Healthcare IT firm needs classy and unique business care design

We need a business card design that incorporates our new logo design (attached) Prefer a purple based designed. I would really love to see something utilizing the "3D" version of the logo (purple on the reflective wall). I want something a little more than my logo printed along with a person's detailed contact information.
Contact Information for Business Card
Want something polished, professional, and a little unique in the design.
Colors
6b449b
Requirements
Must have
- Please use similar font as the logo design
Nice to have
- Would like to see the 3d version of my logo incorporated into the design.

```html
<!DOCTYPE html>
<html lang="en">
<head>
<meta charset="utf-8">
<title>Corvane Health – Business Card</title>
<link href="https://fonts.googleapis.com/css2?family=Montserrat:wght@500;600;700&display=swap" rel="stylesheet">
<style>
  :root {
    --page-bg: #e4e4e6;
    --brand-purple: #6b449b;
    --brand-purple-deep: #5a3788;
    --card-dark: #3a3a3d;
    --text-light: #f4f4f6;
    --text-muted: #c9c9cf;
  }
  * { margin: 0; padding: 0; box-sizing: border-box; }
  html, body {
    width: 1200px;
    height: 1000px;
    overflow: hidden;
    background: var(--page-bg);
    font-family: "Montserrat", sans-serif;
  }
  .card-set {
    position: relative;
    width: 1200px;
    height: 1000px;
  }
  .card {
    position: absolute;
    left: 250px;
    width: 700px;
    height: 400px;
    border-radius: 4px;
    box-shadow: 0 10px 30px rgba(0,0,0,0.18);
  }
  .card-front {
    top: 70px;
    background: var(--brand-purple);
    display: flex;
    align-items: center;
    justify-content: center;
  }
  .brand-name {
    font-weight: 600;
    font-size: 64px;
    letter-spacing: 1px;
    color: var(--brand-purple-deep);
  }
  .card-back {
    top: 530px;
    background: var(--card-dark);
    color: var(--text-light);
  }
  .contact-block {
    position: absolute;
    left: 64px;
    top: 150px;
  }
  .person-name {
    font-weight: 700;
    font-size: 22px;
    letter-spacing: 1px;
    text-transform: uppercase;
  }
  .person-role {
    font-weight: 600;
    font-size: 13px;
    margin-top: 2px;
  }
  .role-rule {
    width: 66px;
    height: 3px;
    background: var(--brand-purple);
    margin-top: 10px;
    margin-bottom: 20px;
  }
  .contact-line {
    font-weight: 500;
    font-size: 16px;
    letter-spacing: 0.5px;
    line-height: 1.45;
  }
  .contact-line .sep { color: var(--text-muted); margin: 0 8px; }
</style>
</head>
<body>
  <div class="card-set">
    <section class="card card-front" aria-label="Card front">
      <span class="brand-name">Corvane Health</span>
    </section>

    <section class="card card-back" aria-label="Card back">
      <div class="contact-block">
        <p class="person-name">Daniel Reyes</p>
        <p class="person-role">Founder &amp; Director</p>
        <div class="role-rule"></div>
        <p class="contact-line">0455 210 784<span class="sep">\</span>daniel@corvane.com.au<span class="sep">\</span>www.corvane.com.au</p>
        <p class="contact-line">4200 Harbour Lane, 18, Westfield, VA 24410</p>
      </div>
    </section>
  </div>
</body>
</html>
```